Kettle Ledger Business Card design

We need a stand out business card design for Accounting practice based in Australia specialising in pubs, clubs and hotels. We help venues maximise margins, create time and manage cashflow. One club we have been working with for the last 6 months has increased revenue by 3% and margin by 5% in this time frame. We have a back office outsourced system that costs less than having a full time employee and also allows the venues the added benefit of:<br/>-using the office space to become a revenue generating opportunity. <br/>-a complete system to enhance governance, accountability and efficiency within their operation<br/>-52 weeks cover so no hassle to cover annual/sick .. leave<br/><br/>We would like to see designs that use the colours of our logo (green & blue).
Target Market(s)
Australian Pubs, Clubs & Hotels abookkeeping, accounting and tax services
Industry/Entity Type
Accountant
Contact Information for Business Card
Miriam Oakley CPA
Principal
Accountant Tax Agent
Miriam@KettleLedger-example.com.au
0418693142
www.kettleledger-example.com.au
Accounting / Payroll / Tax / SMSF / Technology
Colors
Designer to choose colors to be used in the design.
Look and feel
Each slider illustrates characteristics of the customer's brand and the style your logo design should communicate.

```html
<!DOCTYPE html>
<html lang="en">
<head>
<meta charset="utf-8">
<title>Kettle Ledger – Business Card</title>
<link rel="stylesheet" href="https://fonts.googleapis.com/css2?family=Poppins:wght@600&family=Questrial&display=swap">
<style>
  :root {
    --brand-blue: #23418c;
    --brand-green: #146b3a;
    --mint-tint: #d8e8e1;
    --blue-tint: #a7b2d4;
    --paper: #ffffff;
    --card-edge: #1a1a1a;
  }
  * { box-sizing: border-box; margin: 0; padding: 0; }
  html, body { width: 1200px; height: 1200px; overflow: hidden; background: var(--paper); }
  body { position: relative; font-family: "Questrial", sans-serif; }

  .card {
    position: absolute;
    left: 255px;
    width: 729px;
    height: 445px;
    overflow: hidden;
  }
  .card--front { top: 114px; background: var(--paper); border: 1px solid var(--card-edge); }
  .card--back { top: 646px; background: var(--brand-blue); }

  .card__decor { position: absolute; left: 0; top: 0; width: 729px; height: 445px; }

  .brand {
    position: absolute;
    left: 57px;
    top: 58px;
    display: flex;
    align-items: center;
    gap: 18px;
  }
  .brand__dot {
    width: 78px; height: 78px;
    border-radius: 50%;
    background: var(--brand-green);
  }
  .brand__name {
    font-family: "Poppins", sans-serif;
    font-weight: 600;
    font-size: 44px;
    letter-spacing: -0.5px;
    color: var(--brand-blue);
  }

  .person { position: absolute; left: 169px; top: 190px; }
  .person__name {
    font-family: "Poppins", sans-serif;
    font-weight: 600;
    font-size: 26px;
    color: var(--brand-blue);
    line-height: 1.2;
  }
  .person__name .credential { font-family: "Questrial", sans-serif; font-weight: 400; font-style: italic; }
  .person__role { margin-top: 12px; font-size: 21px; color: var(--brand-green); line-height: 27px; }

  .contact { position: absolute; left: 169px; top: 326px; list-style: none; font-size: 21px; line-height: 31.5px; }
  .contact__label { display: inline-block; width: 31px; color: var(--brand-green); }
  .contact__value { color: var(--brand-blue); }

  .services { position: absolute; left: 81px; top: 104px; list-style: none; color: var(--paper); font-size: 30px; line-height: 37px; }
  .services li::before {
    content: ""; display: inline-block;
    width: 11px; height: 11px; border-radius: 50%;
    background: var(--paper); margin-right: 8px; vertical-align: middle;
  }

  .back-url {
    position: absolute; left: 86px; top: 362px;
    font-family: "Poppins", sans-serif; font-weight: 600;
    font-size: 32px; color: var(--paper);
  }
</style>
</head>
<body>

<section class="card card--front" aria-label="Business card front">
  <svg class="card__decor" viewBox="0 0 729 445" aria-hidden="true">
    <circle cx="760" cy="250" r="330" fill="var(--mint-tint)"/>
  </svg>

  <div class="brand">
    <span class="brand__dot"></span>
    <span class="brand__name">Kettle Ledger</span>
  </div>

  <div class="person">
    <p class="person__name">Miriam Oakley <span class="credential">CPA</span></p>
    <p class="person__role">Principal<br>Accountant Tax Agent</p>
  </div>

  <ul class="contact">
    <li><span class="contact__label">E:</span><span class="contact__value">Miriam@KettleLedger-example.com.au</span></li>
    <li><span class="contact__label">T:</span><span class="contact__value">0418693142</span></li>
    <li><span class="contact__label">W:</span><span class="contact__value">www.kettleledger-example.com.au</span></li>
  </ul>
</section>

<section class="card card--back" aria-label="Business card back">
  <svg class="card__decor" viewBox="0 0 729 445" aria-hidden="true">
    <circle cx="760" cy="250" r="330" fill="none" stroke="var(--blue-tint)" stroke-width="24"/>
  </svg>

  <ul class="services">
    <li>Accounting</li>
    <li>Payroll</li>
    <li>Tax</li>
    <li>SMSF</li>
    <li>Technology</li>
  </ul>

  <p class="back-url">www.kettleledger-example.com.au</p>
</section>

</body>
</html>
```